trading data display webpage

We have build a rough wireframe of the two webpages that we want to display .The two wireframes are attached as a pdf document.
there will be login page. after login , the user will see the index page. that is the first page of the wireframe.

what we are displaying is essentially spread data. we are taking the difference in prices are two places and displaying the data. some calculations are done and is shown in the grid.

below the grid we show the behaviour on a graph. we will use bubble chart. I did not find a sample, hence have thrown in a placeholder.

this is time series data ( changes daily) and hence we need to check the behaviour.

the second wire frame shows how the user will choose the source price points and the destination price points.
we are talking here of natural gas prices hence the reference to source prices and destination prices.

you need to design the page/ pages such that the end-user loves it and is easy to use. the intent here is easy to use and easy to understand.
this will be responsive webpage since the end user will check it out on a tablet or a smartphone.

so if possible tell us how the navigation bar, the button bar, etc should fall when the screen size decreases.

I have uploaded 2 files. one is the wireframe ( pdf document) and second is the logo file.

please also let us know where to place the logo.

Target Market(s)

the target market is traders and data analyst

Industry/Entity Type

Build

Colors

Designer to choose colors to be used in the design.

Requirements
Must have
• 1. design for the web.
2. but think how the design will look when the screen size decreases.
3. tell if possible what screen components to keep and what to hide.

```html
<!DOCTYPE html>
<html lang="en">
<head>
<meta charset="utf-8">
<title>Gasline — Spread Dashboard</title>
<link href="https://fonts.googleapis.com/css2?family=Arimo:wght@400;700&display=swap" rel="stylesheet">
<style>
  :root{
    --page:#f1f2f6;
    --ink:#1e1e1e;
    --band-top:#3a3a3a;
    --band-bottom:#151515;
    --btn-top:#4a4a4a;
    --btn-bottom:#1c1c1c;
    --btn-line:#5a5a5a;
    --tab-light-top:#e2e2e2;
    --tab-light-bottom:#b9b9b9;
    --select-bg:#ececec;
    --header-green:#b2d67e;
    --row-a:#e4e4e4;
    --row-b:#dadada;
    --grid-line:#b8b8b8;
    --divider:#bdbdbd;
    --cyan:#5bcbd9;
    --cyan-side:#33a9b8;
    --cyan-top:#4fb9c6;
    --yellow:#e6d77c;
    --red:#e45c5c;
    --logo:#e8672a;
  }
  *{box-sizing:border-box;margin:0;padding:0}
  html,body{width:1200px;height:1011px;overflow:hidden}
  body{position:relative;background:var(--page);font-family:"Arimo",Arial,sans-serif;color:var(--ink);font-size:14px}

  .brand{position:absolute;left:58px;top:44px;display:flex;align-items:center;gap:10px;font-size:26px;font-weight:700;color:var(--logo)}
  .brand-dot{width:26px;height:26px;border-radius:50%;background:var(--logo)}

  .region-tabs{position:absolute;left:23px;top:137px;display:flex}
  .region-tab{width:153px;height:37px;display:flex;align-items:center;justify-content:center;font-size:14px;
    background:linear-gradient(var(--tab-light-top),var(--tab-light-bottom));color:#222;border-right:1px solid #9a9a9a}
  .region-tab.is-active{background:linear-gradient(#6a6a6a,#2e2e2e);color:#fff}

  .control-band{position:absolute;left:0;top:174px;width:1200px;height:121px;background:linear-gradient(var(--band-top),var(--band-bottom))}
  .index-select{position:absolute;height:40px;background:var(--select-bg);border:1px solid #cfcfcf;display:flex;align-items:center;padding-left:21px;font-size:14px;color:#222}
  .index-select svg{position:absolute;right:12px;top:10px}
  .index-select.source{left:21px;top:21px;width:309px}
  .index-select.destination{left:871px;top:21px;width:309px}
  .range-group{position:absolute;top:69px;display:flex;border:1px solid var(--btn-line)}
  .range-group.days{left:21px}
  .range-group.period{left:873px}
  .range-btn{height:38px;display:flex;align-items:center;justify-content:center;color:#eee;font-size:14px;
    background:linear-gradient(var(--btn-top),var(--btn-bottom));border-right:1px solid var(--btn-line)}
  .range-btn:last-child{border-right:0}
  .days .range-btn{width:153px}
  .period .range-btn{width:153px}

  .spread-table{position:absolute;left:0;top:295px;width:1200px;border-collapse:collapse;table-layout:fixed}
  .spread-table th,.spread-table td{text-align:left;font-weight:400;font-size:14px;padding-left:23px;border-right:1px solid var(--grid-line)}
  .spread-table th:last-child,.spread-table td:last-child{border-right:0;padding-left:33px}
  .spread-table th:first-child,.spread-table td:first-child{padding-left:42px}
  .spread-table th{height:55px;background:var(--header-green);color:#222}
  .spread-table td{height:55px;border-top:1px solid #cfcfcf}
  .spread-table tbody tr:nth-child(odd){background:var(--row-a)}
  .spread-table tbody tr:nth-child(even){background:var(--row-b)}

  .chart-panel{position:absolute;top:625px;height:386px}
  .chart-panel.mix{left:0;width:590px;border-right:1px solid var(--divider)}
  .chart-panel.trend{left:591px;width:609px}
  .chart-title{position:absolute;top:40px;width:100%;font-size:14px}
  .mix .chart-title{left:206px}
  .trend .chart-title{left:235px}
  .chart-art{position:absolute;left:0;top:625px}
  .legend{position:absolute;list-style:none}
  .legend li{display:flex;align-items:center;height:40px;font-size:14px}
  .legend i{width:28px;height:27px;margin-right:12px;display:block}
  .mix .legend{left:361px;top:137px}
  .trend .legend{left:431px;top:166px}
</style>
</head>
<body>
  <div class="brand"><span class="brand-dot"></span>Gasline</div>

  <nav class="region-tabs">
    <div class="region-tab is-active">EAST</div>
    <div class="region-tab">CENTRAL</div>
    <div class="region-tab">WEST</div>
  </nav>

  <section class="control-band">
    <div class="index-select source">SOURCE INDICES
      <svg width="18" height="20" viewBox="0 0 18 20"><path d="M9 1 17 8H1Z M1 12H17L9 19Z" fill="#555"/></svg>
    </div>
    <div class="range-group days">
      <div class="range-btn">5 DAYS</div><div class="range-btn">7 DAYS</div><div class="range-btn">18 DAYS</div>
    </div>
    <div class="index-select destination">DESTINATION INDICES
      <svg width="18" height="20" viewBox="0 0 18 20"><path d="M9 1 17 8H1Z M1 12H17L9 19Z" fill="#555"/></svg>
    </div>
    <div class="range-group period">
      <div class="range-btn">MONTH</div><div class="range-btn">YEAR</div>
    </div>
  </section>

  <table class="spread-table">
    <colgroup><col style="width:178px"><col style="width:150px"><col style="width:150px"><col style="width:150px"><col style="width:150px"><col style="width:151px"><col></colgroup>
    <thead><tr><th>SPREAD NAME</th><th>AVG SPREAD</th><th>+ve PROB</th><th>-ve PROB</th><th>SPIKE PROB</th><th>AVG SUPPLY</th><th>SUPPLY CUT_PROB</th></tr></thead>
    <tbody>
      <tr><td>SPREAD 1</td><td>ITEM 1</td><td>ITEM 1</td><td>ITEM 1</td><td>ITEM 1</td><td>ITEM 1</td><td>ITEM 1</td></tr>
      <tr><td>SPREAD 2</td><td>ITEM 2</td><td>ITEM 2</td><td>ITEM 2</td><td>ITEM 2</td><td>ITEM 2</td><td>ITEM 2</td></tr>
      <tr><td>SPREAD 3</td><td>ITEM 3</td><td>ITEM 3</td><td>ITEM 3</td><td>ITEM 3</td><td>ITEM 3</td><td>ITEM 3</td></tr>
      <tr><td>SPREAD 4</td><td>ITEM 4</td><td>ITEM 4</td><td>ITEM 4</td><td>ITEM 4</td><td>ITEM 4</td><td>ITEM 4</td></tr>
      <tr><td>SPREAD 5</td><td>ITEM 5</td><td>ITEM 5</td><td>ITEM 5</td><td>ITEM 5</td><td>ITEM 5</td><td>ITEM 5</td></tr>
    </tbody>
  </table>

  <svg class="chart-art" width="1200" height="386" viewBox="0 625 1200 386">
    <!-- pie -->
    <circle cx="212" cy="835" r="101" fill="var(--cyan)"/>
    <path d="M212 835 L307.5 867.9 A101 101 0 0 1 212 936 Z" fill="var(--yellow)"/>
    <path d="M212 835 L212 936 A101 101 0 0 1 177.5 929.9 Z" fill="var(--red)"/>
    <!-- bar chart frame -->
    <g fill="none" stroke="#c4c4c4" stroke-width="1">
      <path d="M716 747H982V931L972 941H706V757Z"/>
      <path d="M706 757 716 747M716 747V931H982M716 931 706 941"/>
      <path d="M716 779H982M706 789 716 779M716 851H982M706 861 716 851"/>
    </g>
    <g font-family="Arimo, Arial, sans-serif" font-size="13" fill="#222">
      <text x="699" y="794" text-anchor="end">200</text>
      <text x="699" y="866" text-anchor="end">100</text>
      <text x="699" y="946" text-anchor="end">0</text>
      <text x="751" y="958" text-anchor="middle">1</text>
      <text x="809" y="958" text-anchor="middle">2</text>
      <text x="869" y="958" text-anchor="middle">3</text>
    </g>
    <g>
      <path d="M765 803 781 793V931L765 941Z" fill="var(--cyan-side)"/>
      <path d="M729 803 745 793H781L765 803Z" fill="var(--cyan-top)"/>
      <rect x="729" y="803" width="36" height="138" fill="var(--cyan)"/>
      <path d="M825 783 841 773V931L825 941Z" fill="var(--cyan-side)"/>
      <path d="M789 783 805 773H841L825 783Z" fill="var(--cyan-top)"/>
      <rect x="789" y="783" width="36" height="158" fill="var(--cyan)"/>
      <path d="M885 823 901 813V931L885 941Z" fill="var(--cyan-side)"/>
      <path d="M849 823 865 813H901L885 823Z" fill="var(--cyan-top)"/>
      <rect x="849" y="823" width="36" height="118" fill="var(--cyan)"/>
    </g>
  </svg>

  <section class="chart-panel mix">
    <h2 class="chart-title" style="font-weight:400">SPREAD vs SUPPLY</h2>
    <ul class="legend">
      <li><i style="background:var(--cyan)"></i>ONE</li>
      <li><i style="background:var(--yellow)"></i>TWO</li>
      <li><i style="background:var(--red)"></i>THREE</li>
    </ul>
  </section>

  <section class="chart-panel trend">
    <h2 class="chart-title" style="font-weight:400">SPREAD ACROSS TIME</h2>
    <ul class="legend">
      <li><i style="background:var(--cyan)"></i>ONE</li>
    </ul>
  </section>
</body>
</html>
```